Kestrel Aid Services Banner Ad

Need a 750 x 250-pixel banner ad with the company Logo included. Please see company website at www.kestrelaidservices.com for more information.

```html
<!DOCTYPE html>
<html lang="en">
<head>
<meta charset="utf-8">
<title>Kestrel Aid Services Banner</title>
<link rel="stylesheet" href="https://fonts.googleapis.com/css2?family=Poppins:wght@600;700;800&family=Roboto:wght@400&display=swap">
<style>
  :root {
    --page-bg: #e4e4e4;
    --navy-top: #1b5a90;
    --navy-bottom: #0c2f5c;
    --brand-green: #6cc024;
    --brand-blue: #2a78b6;
    --white: #ffffff;
    --photo-top: #a08a72;
    --photo-mid: #c9463a;
    --photo-bottom: #3d5a86;
  }
  * { margin: 0; padding: 0; box-sizing: border-box; }
  html, body { width: 1200px; height: 1200px; overflow: hidden; background: var(--page-bg); }
  .banner {
    position: absolute; left: 45px; top: 418px;
    width: 1110px; height: 363px; overflow: hidden;
    font-family: "Poppins", sans-serif;
  }
  .banner-shapes { position: absolute; inset: 0; }
  .brand {
    position: absolute; left: 40px; top: 34px;
    display: flex; align-items: center; gap: 14px;
  }
  .brand-dot { width: 46px; height: 46px; border-radius: 50%; background: var(--brand-blue); }
  .brand-name {
    color: var(--brand-blue); font-weight: 700; font-size: 27px; line-height: 1.05;
  }
  .headline {
    position: absolute; left: 37px; top: 152px;
    color: var(--white); font-weight: 800; font-size: 23px; line-height: 26px;
    letter-spacing: 0.2px;
  }
  .cta {
    position: absolute; left: 37px; top: 252px;
    width: 201px; height: 32px; border-radius: 16px;
    background: var(--brand-green); color: var(--white);
    font-family: "Roboto", sans-serif; font-size: 17px;
    display: flex; align-items: center; justify-content: center; gap: 8px;
  }
  .cta-icon { width: 16px; height: 16px; }
  .service {
    position: absolute; right: 49px; top: 26px; text-align: right;
  }
  .service-main {
    color: var(--brand-green); font-weight: 800; font-size: 48px; line-height: 46px;
  }
  .service-sub {
    color: var(--brand-blue); font-weight: 800; font-size: 26px; line-height: 28px;
  }
  .region {
    position: absolute; right: 49px; top: 148px; text-align: right;
    color: var(--white); font-weight: 800; font-size: 50px; line-height: 45px;
  }
  .region-line { display: flex; justify-content: flex-end; align-items: center; gap: 10px; }
  .region-tick { width: 44px; height: 34px; }
</style>
</head>
<body>
  <div class="banner">
    <svg class="banner-shapes" width="1110" height="363" viewBox="0 0 1110 363">
      <defs>
        <linearGradient id="navyFade" x1="0" y1="0" x2="0" y2="1">
          <stop offset="0" stop-color="var(--navy-top)"/>
          <stop offset="1" stop-color="var(--navy-bottom)"/>
        </linearGradient>
        <linearGradient id="photoTones" x1="0" y1="0" x2="0" y2="1">
          <stop offset="0" stop-color="var(--photo-top)"/>
          <stop offset="0.55" stop-color="var(--photo-mid)"/>
          <stop offset="1" stop-color="var(--photo-bottom)"/>
        </linearGradient>
      </defs>
      <rect class="panel-navy" width="1110" height="363" fill="url(#navyFade)"/>
      <polygon class="panel-white-left" points="0,0 328,0 289,127 0,127" fill="var(--white)"/>
      <polygon class="panel-white-right" points="756,0 1110,0 1110,127 795,127" fill="var(--white)"/>
      <polygon class="photo-edge" points="361,0 733,0 844,363 249,363" fill="var(--white)"/>
      <polygon class="photo-area" points="365,0 729,0 840,363 254,363" fill="url(#photoTones)"
               role="img" aria-label="Photo of two smiling friends in red jackets sitting together on a park bench, one holding a small yellow flower"/>
    </svg>

    <div class="brand">
      <span class="brand-dot"></span>
      <span class="brand-name">Kestrel Aid<br>Services</span>
    </div>

    <p class="headline">WE CREATE A<br>BRIGHTER<br>FUTURE FOR YOU</p>

    <div class="cta">LEARN MORE
      <svg class="cta-icon" viewBox="0 0 16 16"><circle cx="8" cy="8" r="8" fill="var(--white)"/><path d="M6.5 4.5 L10 8 L6.5 11.5" fill="none" stroke="var(--brand-green)" stroke-width="2.2" stroke-linecap="round" stroke-linejoin="round"/></svg>
    </div>

    <div class="service">
      <div class="service-main">SUPPORT</div>
      <div class="service-sub">COORDINATION</div>
    </div>

    <div class="region">
      <div class="region-line">ACROSS</div>
      <div class="region-line">
        <svg class="region-tick" viewBox="0 0 44 34"><polyline points="6,17 17,28 38,6" fill="none" stroke="var(--brand-green)" stroke-width="7" stroke-linecap="round" stroke-linejoin="round"/></svg>
        NEW</div>
      <div class="region-line">JERSEY</div>
    </div>
  </div>
</body>
</html>
```